New Design for Accounting Firm

CLIENT NAME: Corvanta
CURRENT WEBSITE: www.corvantagroup.example.com.au

CLIENTS THE CLIENT LIKES:
http://velduro.example.se/
http://www.layerport.example.biz/index.php
http://www.plinthworks.example.co.uk/
http://www.worldreliefmonitor.example.org/

COLOUR THEMES:
Colour theme to reflect the logo, with a leaning to blue in Accounting & Audit sections and green in Super section.

LOOK AND FEEL:
The look and feel needs to reflect an accessible culture and contemporary sensibility while still communicating our experience and stability as a professional company.

ABOUT:
The concept of 'Corvanta' is integral to our identity. Definition: 'The connection of creative ideas from a group of diverse individuals, applied with the end aim of solving practical problems'. See ''About Us'' on our website for more.

OTHER DETAILS:
Our three divisions (and service areas within each division) must be easily navigated as they related to very different users of the site. Two client sign in sections (Accounting & Super) must be easily distinguished to avoid user confusion.

MENU STRUCTURE:
* About
- includes history, values, our people, community etc
* Accounting & Advisory
- About
- Services
- Tax & Accounting
- Business Advisory
- Family Wealth Management
- Client Sign In
- Calculators
* Audit & Assurance
- About
- Services
* Corvanta Super
- About
- Individuals
- Services
- Advisers
- Services
- Portal Sign In
- Calculators
* Careers
* Newsletters
* Contact

REQUIREMENTS:
- Layered PSD form home and content pages
- No coding required, we use our own CMS to insert XHTML files into.
Updates

Hi Guys,

The client has asked for a non-cliche'd images in the design. If you'd like to try again with some images that represent the business but aren't your standard boring accounting-looking people, then please do! Cliche is a killer in design - please pump some creativity in!

Cheers,
Ned.

Reason: GUYS - PLEASE LISTEN TO THESE COMMENTS - I'VE SAID THEM TWICE NOW AND PEOPLE ARE STILL POSTING PROJECTS WITH CLICHED AND OBVIOUS ACCOUTNING TYPE IMAGES. USE YOUR CREATIVITY AND POST A DESIGN THAT IS OUTSIDE THE BOX WITH REGARDS TO THE IMAGES YOU ARE USING.

Reason: I am waiting to hear back from the client on their decision.

Industry/Entity Type

Accounting

```html
<!DOCTYPE html>
<html lang="en">
<head>
<meta charset="utf-8">
<title>Corvanta – Accounting and Tax, Audit and Assurance, Self Managed Super</title>
<link href="https://fonts.googleapis.com/css2?family=Arimo:ital,wght@0,400;0,700;1,400&family=PT+Sans:wght@400;700&display=swap" rel="stylesheet">
<style>
  :root {
    --navy: #0d2a6b;
    --blue: #0b4f8a;
    --blue-dark: #083d6e;
    --link: #0a5a94;
    --green: #5aab5e;
    --green-dark: #3f8a44;
    --bullet: #63b567;
    --text: #333333;
    --nav-top: #f4f4f4;
    --nav-bottom: #d9d9d9;
    --footer-bg: #e3e3e3;
    --white: #ffffff;
  }
  * { box-sizing: border-box; margin: 0; padding: 0; }
  html, body { width: 1024px; height: 1200px; overflow: hidden; }
  body {
    position: relative;
    background: var(--white);
    font-family: "Arimo", Arial, sans-serif;
    color: var(--text);
  }
  a { color: inherit; text-decoration: none; }

  /* Header */
  .site-header { position: absolute; top: 0; left: 0; width: 1024px; height: 104px; }
  .brand { position: absolute; left: 62px; top: 16px; display: flex; align-items: center; gap: 14px; }
  .brand-mark { width: 52px; height: 52px; background: var(--blue); }
  .brand-name { font-family: "PT Sans", Arial, sans-serif; font-size: 64px; font-weight: 400; color: var(--blue); letter-spacing: -1px; line-height: 70px; }
  .divisions-tagline { position: absolute; left: 811px; top: 18px; font-family: "PT Sans", Arial, sans-serif; font-size: 17.5px; line-height: 20.5px; color: var(--text); }

  .header-rule { position: absolute; top: 103px; left: 0; width: 1024px; height: 5px;
    background: linear-gradient(90deg, var(--navy) 0%, var(--blue) 25%, var(--green) 55%, var(--blue) 80%, var(--navy) 100%); }

  /* Navigation */
  .main-nav { position: absolute; top: 108px; left: 0; width: 1024px; height: 42px;
    background: linear-gradient(var(--nav-top), var(--nav-bottom)); border-bottom: 1px solid #c8c8c8; }
  .main-nav ul { list-style: none; display: flex; position: absolute; left: 25px; top: 12px; gap: 20px; }
  .main-nav li { font-family: "PT Sans", Arial, sans-serif; font-size: 14.5px; color: var(--text); }
  .enquiry-button { position: absolute; left: 835px; top: 6px; width: 150px; height: 29px; border-radius: 15px;
    background: linear-gradient(#6cbc6c, var(--green-dark)); color: var(--white);
    font-family: "PT Sans", Arial, sans-serif; font-size: 15px; text-align: center; line-height: 28px;
    box-shadow: 0 1px 2px rgba(0,0,0,.3); }

  /* Hero */
  .hero { position: absolute; top: 150px; left: 0; width: 1024px; height: 298px;
    background: radial-gradient(ellipse at 30% 20%, #ffffff 0%, #f1f1f1 55%, #e6e6e6 100%);
    box-shadow: 0 3px 6px rgba(0,0,0,.15); }
  .hero-quote { position: absolute; left: 33px; top: 44px; width: 500px; font-style: italic; font-size: 23.5px; line-height: 29px; color: var(--text); }
  .login-button { position: absolute; top: 216px; height: 46px; width: 267px; border-radius: 23px;
    color: var(--white); font-family: "PT Sans", Arial, sans-serif; font-size: 19px; text-align: center; line-height: 45px;
    box-shadow: 0 3px 4px rgba(0,0,0,.3); }
  .login-accounting { left: 24px; background: linear-gradient(#2472b5, var(--blue-dark)); }
  .login-super { left: 300px; background: linear-gradient(#78c478, var(--green-dark)); }
  .hero-image { position: absolute; left: 618px; top: 4px; width: 382px; height: 288px; border-radius: 40px;
    background: radial-gradient(ellipse at center, #b9bba8 0%, #d3d4c6 45%, rgba(230,230,230,0) 75%); }

  /* Intro */
  .section-title { font-family: "PT Sans", Arial, sans-serif; font-weight: 400; font-size: 18.5px; color: var(--text); }
  .welcome { position: absolute; left: 62px; top: 471px; width: 560px; }
  .welcome p { font-size: 13.3px; line-height: 17px; color: var(--text); margin-top: 6px; }
  .welcome p + p { margin-top: 16px; }
  .services-index { position: absolute; left: 692px; top: 471px; }
  .services-index ul { list-style: none; margin-top: 6px; }
  .services-index li { font-size: 12px; line-height: 14.4px; color: var(--link); letter-spacing: .1px; }

  /* Division columns */
  .division { position: absolute; top: 610px; width: 271px; }
  .division h2 { padding-bottom: 5px; border-bottom: 4px solid var(--blue); white-space: nowrap; }
  .division p { font-size: 11.5px; line-height: 14px; color: var(--text); margin-top: 20px; }
  .division ul { list-style: none; margin-top: 4px; padding-left: 20px; }
  .division li { font-size: 12px; line-height: 20px; color: var(--text); padding-left: 16px; position: relative; }
  .division li.bulleted::before { content: ""; position: absolute; left: 0; top: 7px; width: 7px; height: 7px; border-radius: 50%; background: var(--bullet); }
  .learn-more { display: block; text-align: right; font-size: 12px; color: var(--link); text-decoration: underline; margin-top: 10px; }
  .division-accounting { left: 62px; }
  .division-audit { left: 378px; }
  .division-super { left: 691px; }

  /* Footer sitemap */
  .sitemap { position: absolute; top: 925px; left: 0; width: 1024px; height: 188px; background: var(--footer-bg); border-top: 1px solid #c9c9c9; }
  .sitemap-col { position: absolute; top: 13px; }
  .sitemap-col h3 { font-family: "PT Sans", Arial, sans-serif; font-weight: 400; font-size: 15px; color: var(--text); margin-bottom: 4px; }
  .sitemap-col ul { list-style: none; }
  .sitemap-col li { font-size: 11px; line-height: 18px; color: var(--text); }
  .sitemap-extra { list-style: none; position: absolute; left: 513px; top: 93px; }
  .sitemap-extra li { font-family: "PT Sans", Arial, sans-serif; font-size: 15px; line-height: 20px; color: var(--text); }

  /* Bottom bar */
  .legal { position: absolute; top: 1113px; left: 0; width: 1024px; height: 87px;
    background: linear-gradient(90deg, #133a66 0%, #265a72 45%, #3f8a6c 75%, #60ad68 100%);
    color: var(--white); padding: 10px 0 0 21px; font-size: 12px; line-height: 20px; }
  .legal strong { font-weight: 700; }
  .legal .gap { display: inline-block; width: 20px; }
</style>
</head>
<body>

<header class="site-header">
  <a class="brand" href="#">
    <span class="brand-mark"></span>
    <span class="brand-name">Corvanta</span>
  </a>
  <p class="divisions-tagline">Accounting and Tax<br>Audit and Assurance<br>Self Managed Super</p>
</header>
<div class="header-rule"></div>

<nav class="main-nav">
  <ul>
    <li><a href="#">Home</a></li>
    <li><a href="#">About</a></li>
    <li><a href="#">Accounting &amp; Advisory</a></li>
    <li><a href="#">Audit &amp; Assurance</a></li>
    <li><a href="#">Corvanta Super</a></li>
    <li><a href="#">Careers</a></li>
    <li><a href="#">Newsletters</a></li>
    <li><a href="#">Contact</a></li>
  </ul>
  <a class="enquiry-button" href="#">Send an Enquiry</a>
</nav>

<section class="hero">
  <blockquote class="hero-quote">“The connection of creative ideas from a group of diverse individuals, applied with the end aim of solving practical problems”</blockquote>
  <a class="login-button login-accounting" href="#">Accounting Client Login</a>
  <a class="login-button login-super" href="#">Corvanta Super Portal Login</a>
  <div class="hero-image" role="img" aria-label="Jigsaw puzzle pieces made from banknotes fitting together"></div>
</section>

<section class="welcome">
  <h1 class="section-title">Welcome to Corvanta</h1>
  <p><strong>Corvanta</strong> is a Kestrel Coast based firm which offers the skills of Accountants, Business Performance Advisers, Auditors and Self Managed Super Fund Specialists.</p>
  <p>From our offices in Marrowby and Eastholme we deliver services across three divisions:</p>
</section>

<aside class="services-index">
  <h2 class="section-title">Services</h2>
  <ul>
    <li><a href="#">Accounting and Taxation</a></li>
    <li><a href="#">Corporate and Business Advice</a></li>
    <li><a href="#">Family Wealth Management</a></li>
    <li><a href="#">Audit and Assurance</a></li>
    <li><a href="#">Self Managed Super Fund Administration</a></li>
  </ul>
</aside>

<section class="division division-accounting">
  <h2 class="section-title">RL Corvanta Chartered Accountants</h2>
  <p>Our Accounting and Advisory team - RL Corvanta Chartered Accountants - provide traditional accounting services and professional corporate and business advice. Our services include:</p>
  <ul>
    <li class="bulleted">Accounting and Taxation Services</li>
    <li class="bulleted">Corporate and Business Advice</li>
    <li class="bulleted">Family Wealth Management</li>
  </ul>
  <a class="learn-more" href="#">Learn More</a>
</section>

<section class="division division-audit">
  <h2 class="section-title">Corvanta Audit &amp; Assurance</h2>
  <p>The services provided by Corvanta Audit &amp; Assurance Pty Ltd include:</p>
  <ul>
    <li class="bulleted">Financial Statement audits</li>
    <li class="bulleted">Reviews of Financial Reports</li>
    <li class="bulleted">Internal audits</li>
    <li class="bulleted">Systems and controls reviews</li>
    <li class="bulleted">Taxation compliance reviews</li>
    <li class="bulleted">Self Managed Super Fund audits</li>
    <li class="bulleted">Corporate Super Fund audits</li>
    <li class="bulleted">Trust Account audits</li>
    <li class="bulleted">Grant Aquittal Reports</li>
  </ul>
  <a class="learn-more" href="#">Learn More</a>
</section>

<section class="division division-super">
  <h2 class="section-title">Corvanta Super</h2>
  <p>Services include:</p>
  <ul>
    <li class="bulleted">super fund establishment</li>
    <li class="bulleted">administration</li>
    <li class="bulleted">audit</li>
    <li class="bulleted">trust deed review</li>
    <li class="bulleted">pension establishment</li>
    <li>binding death beneficiary nominations</li>
    <li class="bulleted">investment strategies</li>
    <li class="bulleted">trustee minutes.</li>
  </ul>
  <a class="learn-more" href="#">Learn More</a>
</section>

<footer>
  <div class="sitemap">
    <div class="sitemap-col" style="left:22px">
      <h3>About</h3>
      <ul><li>History</li><li>Values</li><li>Our People</li><li>Community</li></ul>
    </div>
    <div class="sitemap-col" style="left:145px">
      <h3>Accounting &amp; Advisory</h3>
      <ul><li>About</li><li>Services</li><li>Tax &amp; Accounting</li><li>Business Advisory</li><li>Family Wealth Management</li><li>Client Sign In</li><li>Calculators</li></ul>
    </div>
    <div class="sitemap-col" style="left:352px">
      <h3>Corvanta Super</h3>
      <ul><li>About</li><li>Individuals</li><li>Services</li><li>Advisers</li><li>Services</li><li>Portal Sign In</li><li>Calculators</li></ul>
    </div>
    <div class="sitemap-col" style="left:513px">
      <h3>Audit &amp; Assurance</h3>
      <ul><li>About</li><li>Services</li></ul>
    </div>
    <ul class="sitemap-extra"><li>Careers</li><li>Newsletters</li><li>Contact</li></ul>
  </div>
  <div class="legal">
    <strong>© 2011 Corvanta</strong><br>
    123 Your Address 123456 CITY-COUNTRY<br>
    Tél : 01 23 45 67 89<span class="gap"></span>Fax : 01 23 45 67 89
  </div>
</footer>

</body>
</html>
```